BRIGHTWELL PARTNERS POWERPOINT PRESENTATION TEMPLATE 1

We need the ultimate quality Powerpoint presentation design.
We are the advisory firm working with modern world class tech companies throughout Europe, their founders, shareholders, and potential investors.
The new template must contain elements such as our logo, appropriate backgrounds, be at the same time very attractive visually and easy to rear. Also there must be some place where logo of our clients should be placed.

We like:
- icons and
- infographics,
so attractive design in this area will be greatly appreciated.

Please avoid serif fonts and excessive decorations such as "waves" or other similar decor.

We are also in contact with serious investors - wealthy individuals, reputable financial institutions, and their advisers; banks, private equity investors, global technology companies.

The Powerpoint template design must send a message that:
- we are a high technology oriented team of professionals,
- we provide modern financial advisory services
- but at the same time we are open minded, creative, yet very competent in the area of corporate finance.

The Powerpoint template must complement our business card design, first impression of a team of top notch professionals who advise top notch tech companies on their top notch corporate finance and M&A projects.

Enclosed are sets of our logo, current template, business card project which won previous competition.

It is perhaps a good basis to start with and get us to the template of our dreams.

While working on this project please think about the following firms which at some point may be looking at your design:
- Quorra
- Veltrix
- Pondero
- Zentaro (Brixel)
- Moodlane
- Kurotan
- Wavoro
- Dalvion
- Strelo

The quality of the design, its style, aesthetics must meet the top criteria in contemporary design trends.

Target Market(s)

Banks, financial investors, strategic investors

Industry/Entity Type

Finance

Font styles to use
Sans Serif

Requirements
Must have
• Icons
Infographics
Attractive backgrounds
Clean design
Harmonize with logo and emblem colors.
Should not have
• Excessive tacky decor (waves, etc)
Serif fonts
Excessive colors

```html
<!DOCTYPE html>
<html lang="en">
<head>
<meta charset="utf-8">
<title>Brightwell Partners – Presentation Template</title>
<link rel="stylesheet" href="https://fonts.googleapis.com/css2?family=Open+Sans:wght@300;400;600;700;800&display=swap">
<style>
  :root {
    --stage: #2b2b2b;
    --navy: #0f2a5c;
    --blue: #1c62b5;
    --blue-deep: #123f8e;
    --blue-light: #2a7fd0;
    --text: #4a4a4a;
    --muted: #9aa3ad;
    --ghost: #d9dde3;
    --card: #eeeff1;
    --line: #b7bcc3;
  }
  * { box-sizing: border-box; }
  html, body { margin: 0; padding: 0; }
  body {
    width: 1200px; height: 777px; overflow: hidden; position: relative;
    background: var(--stage); font-family: 'Open Sans', sans-serif;
  }
  .page-label { position: absolute; color: #fff; font-size: 13px; font-weight: 600; }
  .slide-frame { position: absolute; width: 524px; height: 294.4px; overflow: hidden; }
  .slide {
    position: absolute; left: 0; top: 0; width: 1040px; height: 584px;
    transform: scale(0.504); transform-origin: 0 0; overflow: hidden; background: #fff;
  }
  .abs { position: absolute; }

  /* brand */
  .brand-name { color: var(--navy); font-weight: 400; letter-spacing: -0.01em; white-space: nowrap; }
  .brand-small { left: 38px; top: 36px; font-size: 21px; }
  .header-rule { height: 2px; background: var(--blue); top: 55px; }

  /* footer band */
  .footer-band { left: 0; top: 528px; width: 1040px; height: 56px; }
  .page-num {
    left: 38px; top: 522px; width: 46px; height: 46px; border-radius: 50%;
    background: #fff; color: var(--text); font-size: 18px;
    display: flex; align-items: center; justify-content: center;
  }
  .site-url {
    right: 40px; top: 546px; color: #fff; font-size: 13px; font-weight: 700;
    letter-spacing: 0.62em;
  }

  /* page 1 */
  .cover-brand { left: 58px; top: 152px; font-size: 56px; font-weight: 300; color: var(--navy); }
  .cover-title { left: 58px; top: 262px; font-size: 38px; line-height: 38px; font-weight: 800; color: #1a4f9e; margin: 0; }
  .cover-body { left: 58px; top: 358px; width: 402px; font-size: 15.5px; line-height: 18px; color: var(--text); margin: 0; text-align: justify; }
  .cover-date { left: 58px; top: 455px; font-size: 17px; font-weight: 600; color: var(--muted); }
  .cover-url { left: 60px; top: 516px; color: #fff; font-size: 16px; font-weight: 700; letter-spacing: 0.72em; }

  /* page 2 */
  .disclaimer-title { left: 56px; top: 100px; font-size: 72px; font-weight: 800; color: var(--ghost); letter-spacing: 0.01em; margin: 0; }
  .title-rule { height: 3px; background: var(--blue); width: 86px; }
  .disclaimer-body { left: 61px; top: 234px; width: 428px; }
  .disclaimer-body p { margin: 0 0 12px; font-size: 13.6px; line-height: 16.2px; color: var(--text); text-align: justify; }

  /* page 3 */
  .toc-title { left: 40px; top: 228px; font-size: 50px; line-height: 48px; font-weight: 800; color: #1e68bb; margin: 0; }
  .toc-col { top: 76px; width: 220px; }
  .toc-col h3 {
    position: relative; margin: 0 0 2px; padding-left: 22px; font-size: 12.5px; line-height: 14.5px;
    font-weight: 700; color: var(--blue-light); text-transform: uppercase;
  }
  .toc-col h3::before {
    content: ""; position: absolute; left: 0; top: 2px; width: 11px; height: 11px; background: var(--blue-light);
  }
  .toc-col ul { margin: 0 0 16px; padding: 0 0 0 22px; list-style: none; }
  .toc-col li { position: relative; font-size: 12.8px; line-height: 15.5px; color: var(--text); margin-bottom: 4px; }
  .toc-col li::before { content: "•"; position: absolute; left: -18px; color: #333; }

  /* page 4 */
  .section-tab { left: 738px; top: 0; width: 302px; height: 56px; }
  .section-tab-text { right: 48px; top: 12px; color: #fff; font-size: 24px; font-weight: 700; }
  .intro-heading { font-size: 16px; font-weight: 700; color: var(--blue-light); margin: 0; white-space: nowrap; }
  .sub-heading { font-size: 12.5px; font-weight: 700; color: var(--blue-deep); margin: 0; }
  .info-row { left: 38px; width: 420px; display: flex; gap: 6px; }
  .info-label {
    width: 108px; background: var(--blue); color: #fff; font-size: 12px; font-weight: 700;
    display: flex; align-items: center; justify-content: center; text-align: center; line-height: 13px;
  }
  .info-value {
    flex: 1; border: 1px solid var(--line); font-size: 10.5px; color: var(--text);
    display: flex; align-items: center; justify-content: center;
  }
  .overview-list { left: 38px; top: 328px; width: 440px; margin: 0; padding: 0 0 0 14px; list-style: none; }
  .overview-list li { position: relative; font-size: 10.4px; line-height: 12.8px; color: var(--text); margin-bottom: 6.6px; }
  .overview-list li::before { content: "•"; position: absolute; left: -12px; }
  .activity-card { top: 136px; width: 158px; height: 186px; background: var(--card); text-align: center; padding: 12px 12px 0; }
  .activity-card svg { display: block; margin: 0 auto; }
  .activity-card h4 { margin: 8px 0 6px; font-size: 11.5px; line-height: 13px; font-weight: 700; color: var(--blue-light); }
  .activity-card p { margin: 0; font-size: 10.4px; line-height: 12.5px; color: var(--text); text-align: justify; text-align-last: center; }
  .kpi { width: 206px; height: 34px; display: flex; }
  .kpi-value {
    width: 56px; background: var(--blue); color: #fff; font-size: 13px; font-weight: 700;
    display: flex; align-items: center; justify-content: center;
  }
  .kpi-note {
    flex: 1; border: 1px solid var(--line); font-size: 9.5px; line-height: 10.5px; color: var(--text);
    display: flex; align-items: center; justify-content: center; text-align: center; padding: 0 6px;
  }
  .kpi-icon { width: 28px; height: 28px; }
</style>
</head>
<body>

<svg width="0" height="0" style="position:absolute" aria-hidden="true">
  <defs>
    <linearGradient id="bandGrad" x1="0" y1="0" x2="1" y2="0">
      <stop offset="0" stop-color="#1d64b8"/>
      <stop offset="1" stop-color="#123f8e"/>
    </linearGradient>
    <linearGradient id="discGrad" x1="0" y1="0" x2="0.4" y2="1">
      <stop offset="0" stop-color="#2479cc"/>
      <stop offset="1" stop-color="#0f3c86"/>
    </linearGradient>
    <linearGradient id="photoGrad" x1="0" y1="0" x2="0" y2="1">
      <stop offset="0" stop-color="#d2d2d2"/>
      <stop offset="0.45" stop-color="#8e8e8e"/>
      <stop offset="1" stop-color="#4a4a4a"/>
    </linearGradient>
    <g id="footer">
      <rect x="0" y="0" width="1040" height="56" fill="url(#bandGrad)"/>
      <polygon points="0,0 90,0 130,56 0,56" fill="#2f86d6" opacity="0.55"/>
    </g>
    <g id="iconPeople" fill="#7b7f86">
      <circle cx="7" cy="6" r="3"/><rect x="4" y="10" width="6" height="12" rx="2"/>
      <circle cx="16" cy="5" r="3"/><rect x="13" y="9" width="6" height="13" rx="2"/>
      <circle cx="25" cy="6" r="3"/><rect x="22" y="10" width="6" height="12" rx="2"/>
      <polyline points="2,24 12,16 19,20 31,8" fill="none" stroke="#7b7f86" stroke-width="2"/>
    </g>
    <g id="iconPerson" fill="#7b7f86">
      <circle cx="16" cy="6" r="5"/><path d="M7 30 V19 a9 8 0 0 1 18 0 V30 Z"/>
    </g>
    <g id="iconTarget" fill="none" stroke="#7b7f86" stroke-width="2">
      <circle cx="16" cy="16" r="11"/><circle cx="16" cy="16" r="5"/>
      <line x1="16" y1="1" x2="16" y2="31"/><line x1="1" y1="16" x2="31" y2="16"/>
    </g>
    <g id="iconPin" fill="none" stroke="#7b7f86" stroke-width="2">
      <path d="M10 28 C4 20 3 16 3 12 a7 7 0 0 1 14 0 c0 4 -1 8 -7 16 Z"/><circle cx="10" cy="12" r="2.5"/>
      <path d="M24 20 C20 15 19 12 19 10 a5 5 0 0 1 10 0 c0 2 -1 5 -5 10 Z"/>
    </g>
    <g id="iconBuilding" fill="#7b7f86">
      <rect x="9" y="3" width="14" height="27"/>
      <g fill="#fff"><rect x="12" y="7" width="3" height="3"/><rect x="17" y="7" width="3" height="3"/><rect x="12" y="13" width="3" height="3"/><rect x="17" y="13" width="3" height="3"/><rect x="12" y="19" width="3" height="3"/><rect x="17" y="19" width="3" height="3"/></g>
    </g>
  </defs>
</svg>

<div class="page-label" style="left:59.5px;top:50px">Page 1</div>
<div class="page-label" style="left:623.5px;top:50px">Page 2</div>
<div class="page-label" style="left:59.5px;top:401px">Page 3</div>
<div class="page-label" style="left:623.5px;top:401px">Page 4</div>

<!-- Page 1: cover -->
<div class="slide-frame" style="left:59.5px;top:81.7px">
  <section class="slide cover">
    <svg class="abs" style="left:0;top:0" width="1040" height="584" aria-hidden="true">
      <circle cx="905" cy="300" r="330" fill="url(#discGrad)"/>
      <polygon points="0,497 610,497 650,556 0,556" fill="url(#bandGrad)"/>
    </svg>
    <div class="abs brand-name cover-brand">BRIGHTWELL</div>
    <h1 class="abs cover-title">LOREM IPSUM IS<br>SIMPLY DUMMY TEXT</h1>
    <p class="abs cover-body">Lorem Ipsum is simply dummy text of the printing and typesetting industry. Lorem Ipsum has been the industry's standard dummy text ever since the 1500s,</p>
    <div class="abs cover-date">MONTH | YEAR GOES HERE</div>
    <div class="abs cover-url">WWW.BRIGHTWELL-PARTNERS.EU</div>
  </section>
</div>

<!-- Page 2: disclaimer -->
<div class="slide-frame" style="left:623.5px;top:81.7px">
  <section class="slide disclaimer">
    <svg class="abs" style="left:0;top:0" width="1040" height="584">
      <path d="M552 0 C606 150 612 380 410 528 L1040 528 L1040 0 Z" fill="url(#photoGrad)" role="img" aria-label="Black and white photograph of a city skyline with a stadium and cable-stayed bridge"/>
      <path d="M552 0 C606 150 612 380 410 528" fill="none" stroke="#1c62b5" stroke-width="9"/>
      <use href="#footer" y="528"/>
    </svg>
    <div class="abs brand-name brand-small">BRIGHTWELL</div>
    <div class="abs header-rule" style="left:210px;width:345px"></div>
    <h1 class="abs disclaimer-title">DISCLAIMER</h1>
    <div class="abs title-rule" style="left:64px;top:191px"></div>
    <div class="abs disclaimer-body">
      <p>Lorem Ipsum is simply dummy text of the printing and typesetting industry. Lorem Ipsum has been the industry's standard dummy text ever since the 1500s, when an unknown printer took a galley of type and scrambled it to make a type specimen book. Lorem Ipsum is simply dummy text of the printing and typesetting industry. Lorem Ipsum has been the industry's standard dummy text ever since the 1500s, when an unknown printer took a galley of type and scrambled it to make a type specimen book.</p>
      <p>Lorem Ipsum is simply dummy text of the printing and typesetting industry. Lorem Ipsum has been the industry's standard dummy text ever since the 1500s, when an unknown printer took a galley of type and scrambled it to make a type specimen book.</p>
    </div>
    <div class="abs page-num">01</div>
    <div class="abs site-url">WWW.BRIGHTWELL-PARTNERS.EU</div>
  </section>
</div>

<!-- Page 3: table of contents -->
<div class="slide-frame" style="left:59.5px;top:432.5px">
  <section class="slide contents">
    <svg class="abs" style="left:0;top:0" width="1040" height="584" aria-hidden="true"><use href="#footer" y="528"/></svg>
    <div class="abs brand-name brand-small">BRIGHTWELL</div>
    <div class="abs header-rule" style="left:210px;width:830px"></div>
    <h1 class="abs toc-title">TABLE OF<br>CONTENTS</h1>
    <div class="abs title-rule" style="left:42px;top:336px"></div>

    <div class="abs toc-col" style="left:358px">
      <h3>Introduction</h3>
      <ul><li>Introduction</li><li>Basic Information</li><li>Business development</li><li>Development plans</li><li>Investment thesis</li></ul>
      <h3>Company operations</h3>
      <ul><li>Product portfolio I</li><li>Product description</li><li>Production sites</li><li>Licenses and certificates</li><li>Business model</li><li>Marketing strategy</li><li>Customer groups</li><li>Sales structure</li><li>Key Suppliers and Business Partners</li><li>Raw Materials</li><li>Key people and Organisational structure</li></ul>
    </div>
    <div class="abs toc-col" style="left:590px">
      <h3>Market and competition</h3>
      <ul><li>Market overview</li><li>Market competition</li><li>Company's competitive advantages</li></ul>
      <h3>Strategy and<br>development plans</h3>
      <ul><li>Strategy and development plan</li><li>Acquisition opportunities</li><li>Value proposition</li><li>SWOT analysis</li><li>Capex and investment effects</li></ul>
      <h3>Financial information<br>and forecasts</h3>
      <ul><li>Income Statement</li><li>Revenues structure</li><li>Operating sosts</li><li>Cost of Goods Sold</li><li>Sales profitability</li><li>Cash Flow Statement</li><li>Planned CAPEX</li><li>Balance Sheet</li></ul>
    </div>
    <div class="abs toc-col" style="left:838px">
      <h3>Attachments</h3>
      <ul><li>Financial Statements</li><li>Glossary</li></ul>
    </div>

    <div class="abs page-num">02</div>
    <div class="abs site-url">WWW.BRIGHTWELL-PARTNERS.EU</div>
  </section>
</div>

<!-- Page 4: introduction -->
<div class="slide-frame" style="left:623.5px;top:432.5px">
  <section class="slide introduction">
    <svg class="abs" style="left:0;top:0" width="1040" height="584" aria-hidden="true">
      <polygon points="738,56 778,0 1040,0 1040,56" fill="url(#bandGrad)"/>
      <use href="#footer" y="528"/>
    </svg>
    <div class="abs section-tab-text">INTRODUCTION</div>
    <div class="abs brand-name brand-small">BRIGHTWELL</div>
    <div class="abs header-rule" style="left:210px;width:530px"></div>

    <h2 class="abs intro-heading" style="left:38px;top:98px">[BRIEF DESCRIPTION OF THE COMPANY'S ACTIVITIES]</h2>
    <h3 class="abs sub-heading" style="left:38px;top:139px">BASIC INFORMATION</h3>
    <div class="abs info-row" style="top:162px;height:24px"><div class="info-label">Headquarters</div><div class="info-value">[address]</div></div>
    <div class="abs info-row" style="top:192px;height:24px"><div class="info-label">Industry</div><div class="info-value">Name of the industry</div></div>
    <div class="abs info-row" style="top:221px;height:24px"><div class="info-label">Headcount</div><div class="info-value">No of employee</div></div>
    <div class="abs info-row" style="top:251px;height:38px">
      <div class="info-label">Ownership<br>Structure</div>
      <div class="info-value">
        <svg width="300" height="34" viewBox="0 0 300 34" role="img" aria-label="Ownership pie chart">
          <text x="52" y="14" font-size="6.5" fill="#444" font-family="Open Sans, sans-serif">25.00%</text>
          <text x="52" y="27" font-size="6.5" fill="#444" font-family="Open Sans, sans-serif">25.00%</text>
          <circle cx="92" cy="17" r="9" fill="none" stroke="#f2c230" stroke-width="3.5" stroke-dasharray="28.3 56.5"/>
          <circle cx="92" cy="17" r="9" fill="none" stroke="#7a3ec8" stroke-width="3.5" stroke-dasharray="14.1 56.5" stroke-dashoffset="-28.3"/>
          <circle cx="92" cy="17" r="9" fill="none" stroke="#c5c8ce" stroke-width="3.5" stroke-dasharray="14.1 56.5" stroke-dashoffset="-42.4"/>
          <text x="110" y="20" font-size="6.5" fill="#444" font-family="Open Sans, sans-serif">50.00%</text>
          <g font-size="6" fill="#444" font-family="Open Sans, sans-serif">
            <rect x="176" y="6" width="3" height="3" fill="#f2c230"/><text x="181" y="9">Shareholder 1</text>
            <rect x="176" y="15" width="3" height="3" fill="#7a3ec8"/><text x="181" y="18">Shareholder 2</text>
            <rect x="176" y="24" width="3" height="3" fill="#c5c8ce"/><text x="181" y="27">Shareholder 3</text>
          </g>
        </svg>
      </div>
    </div>

    <h3 class="abs sub-heading" style="left:38px;top:307px">COMPANY'S OVERVIEW</h3>
    <ul class="abs overview-list">
      <li>[key data from the entire presentation]</li>
      <li>XXX is a manufacturer of high quality products A, B, C etc..</li>
      <li>Planned tripling of revenues and quadrupling of EBITDA over [x] years</li>
      <li>The development strategy assumes introducing new product lines and expansion into foreign markets XXX</li>
      <li>[The company has a unique business model based on the...]</li>
      <li>The XXX Team is a combination of business experience, design &amp; sales skills</li>
      <li>XXX</li>
    </ul>

    <h2 class="abs intro-heading" style="left:536px;top:98px">[BRIEF DESCRIPTION OF THE COMPANY'S ACTIVITIES]</h2>
    <div class="abs activity-card" style="left:521px">
      <svg width="40" height="36" viewBox="0 0 32 30"><use href="#iconPeople"/></svg>
      <h4>GRAPHICS/PHOTO<br>/SHAPE</h4>
      <p>Lorem Ipsum is simply dummy text of the printing and typesetting industry. Lorem Ipsum has been the industry's standard dummy text ever since the 1500s,</p>
    </div>
    <div class="abs activity-card" style="left:685px">
      <svg width="40" height="36" viewBox="0 0 32 32"><use href="#iconPerson"/></svg>
      <h4>GRAPHICS/PHOTO<br>/SHAPE</h4>
      <p>Lorem Ipsum is simply dummy text of the printing and typesetting industry. Lorem Ipsum has been the industry's standard dummy text ever since the 1500s,</p>
    </div>
    <div class="abs activity-card" style="left:849px">
      <svg width="40" height="36" viewBox="0 0 32 32"><use href="#iconTarget"/></svg>
      <h4>GRAPHICS/PHOTO<br>/SHAPE</h4>
      <p>Lorem Ipsum is simply dummy text of the printing and typesetting industry. Lorem Ipsum has been the industry's standard dummy text ever since the 1500s,</p>
    </div>

    <h3 class="abs" style="left:536px;top:330px;margin:0;font-size:17px;font-weight:700;color:var(--blue-light)">KPI'S</h3>

    <svg class="abs kpi-icon" style="left:536px;top:373px" viewBox="0 0 32 30"><use href="#iconPeople"/></svg>
    <div class="abs kpi" style="left:575px;top:370px"><div class="kpi-value">XX</div><div class="kpi-note">[employment increase]</div></div>
    <svg class="abs kpi-icon" style="left:536px;top:421px" viewBox="0 0 32 30"><use href="#iconPin"/></svg>
    <div class="abs kpi" style="left:575px;top:418px"><div class="kpi-value">&gt;XXX</div><div class="kpi-note">[products sold]</div></div>
    <svg class="abs kpi-icon" style="left:536px;top:470px" viewBox="0 0 32 32"><use href="#iconBuilding"/></svg>
    <div class="abs kpi" style="left:575px;top:467px"><div class="kpi-value">XX</div><div class="kpi-note">[number of production sites]</div></div>

    <svg class="abs kpi-icon" style="left:774px;top:373px" viewBox="0 0 32 32"><use href="#iconPerson"/></svg>
    <div class="abs kpi" style="left:811px;top:370px"><div class="kpi-value">XX%</div><div class="kpi-note">[increase in the number of clients]</div></div>
    <svg class="abs kpi-icon" style="left:774px;top:421px" viewBox="0 0 32 32"><use href="#iconTarget"/></svg>
    <div class="abs kpi" style="left:811px;top:418px"><div class="kpi-value">X,XX</div><div class="kpi-note">[average number of recipients]</div></div>
    <svg class="abs kpi-icon" style="left:774px;top:470px" viewBox="0 0 32 32"><use href="#iconTarget"/></svg>
    <div class="abs kpi" style="left:811px;top:467px"><div class="kpi-value">XXX</div><div class="kpi-note">[speed of order execution]</div></div>

    <div class="abs page-num">03</div>
    <div class="abs site-url">WWW.BRIGHTWELL-PARTNERS.EU</div>
  </section>
</div>

</body>
</html>
```